Copper Heron Bar & Grill Takeout Menu

Please create a takeout menu using the attached dine-in menu.
Take out menu size: Tri-Fold 11x17

Industry/Entity Type

Bar & Grill (Restaurant)

Colors

Designer to choose colors to be used in the design.

Requirements
Must have
• Phone number and website. "Order Online" "Order for Delivery"
Nice to have
• Area on the back of the menu to feature happy hour specials.

```html
<!DOCTYPE html>
<html lang="en">
<head>
<meta charset="utf-8">
<title>Copper Heron Bar &amp; Grill – Takeout Menu</title>
<link rel="stylesheet" href="https://fonts.googleapis.com/css2?family=Almendra+SC&family=Cabin+Condensed:wght@400;500;600;700&family=Montserrat:wght@900&family=Righteous&display=swap">
<style>
:root{
  --backdrop:#e4e4e6;
  --ink:#202125;
  --box:#151619;
  --yellow:#fccd3f;
  --cyan:#50d8e1;
  --white:#ffffff;
  --muted:#d7d7d7;
  --paw:rgba(0,0,0,.28);
}
*{margin:0;padding:0;box-sizing:border-box}
html,body{width:1018px;height:1200px;overflow:hidden;background:var(--backdrop)}
body{position:relative;font-family:"Cabin Condensed",Arial,sans-serif;color:var(--white)}
.sheet{position:absolute;left:91px;width:836px;background:var(--ink);box-shadow:0 6px 14px rgba(0,0,0,.35);overflow:hidden}
.sheet--outside{top:57px;height:540px}
.sheet--inside{top:617px;height:540px}
.abs{position:absolute}
.box{position:absolute;background:var(--box);border-radius:6px}
.section-title{font-family:"Almendra SC",Georgia,serif;color:var(--yellow);font-size:15px;letter-spacing:.5px;line-height:1}
.note{font-size:6.6px;line-height:8.4px;color:var(--muted)}
.item{display:flex;align-items:baseline;font-weight:600;font-size:7.2px;line-height:9.5px}
.item .dots{flex:1;border-bottom:1px dotted var(--white);margin:0 2px 2px}
.desc{font-size:7px;line-height:9.4px;color:var(--muted);font-weight:400}
.small-desc{font-size:5px;line-height:6.2px;color:#bdbdbd}
.footnote{position:absolute;width:200px;text-align:center;font-size:4.8px;line-height:6.4px;color:#cfcfcf}
.placeholder-yellow{position:absolute;background:var(--yellow);border-radius:45%}
.placeholder-dark{position:absolute;background:#0d0d0f;border-radius:45%}
.paw-field{position:absolute;background:var(--paw);border-radius:10px}

/* outside: left panel */
.handhelds{left:66px;top:11px;width:195px;height:234px;padding:10px 10px 0 12px}
.handhelds .intro{font-size:7px;line-height:9.4px;color:var(--muted);margin:8px 0 12px}
.handhelds .entry{margin-bottom:5px}
.handhelds .item{font-size:7.2px}
.outlined{position:absolute;border:1px solid var(--yellow);border-radius:4px;padding:3px 4px}
.outlined h4{font-family:"Almendra SC",Georgia,serif;font-weight:400;font-size:9.5px;color:var(--white);line-height:1}
.outlined p{font-size:4.4px;line-height:5.6px;color:#cfcfcf;margin-top:1px}
.sides{left:27px;top:350px;width:193px;height:54px;padding:7px 11px}
.sides p{font-size:7.6px;line-height:10.5px;font-weight:600;margin-top:2px}
.kids{left:27px;top:409px;width:193px;height:90px;padding:8px 11px}
.kids .sub{font-size:7px;color:var(--muted);margin:1px 0 5px}
.kids .item{line-height:13.6px}

/* outside: middle panel */
.happy{left:284px;top:23px;width:267px;height:98px;border:1px solid #9a9a9a;background:#141518;text-align:center;padding-top:14px}
.happy h2{font-family:"Montserrat",Arial,sans-serif;font-weight:900;font-size:31px;line-height:28px;letter-spacing:-.5px}
.happy .l1{color:var(--cyan)}
.happy .l2{color:var(--yellow);font-size:40px;line-height:38px}
.lorem-box{left:282px;top:132px;width:269px;height:103px;padding:14px 16px;text-align:center}
.lorem-box p{font-size:6.4px;line-height:9px;color:var(--muted);margin-bottom:9px}
.promo{position:absolute;top:245px;width:125px;height:108px;border-radius:6px;padding:10px 9px;color:var(--ink);font-weight:700;font-size:7px;line-height:9.8px}
.promo--yellow{left:284px;background:var(--yellow)}
.promo--cyan{left:419px;background:var(--cyan)}
.lorem-para{left:284px;top:371px;width:267px;font-size:6.9px;line-height:9.6px;color:var(--muted)}
.delivery-band{left:284px;top:424px;width:267px;height:117px}
.delivery-band .text{position:absolute;left:79px;top:40px;color:var(--ink)}
.delivery-band h3{font-family:"Righteous",Arial,sans-serif;font-weight:400;font-size:19.5px;line-height:22px;letter-spacing:.5px}
.delivery-band .url,.delivery-band .phone{font-family:"Righteous",Arial,sans-serif;font-size:12.5px;line-height:16px}

/* outside: right panel (cover) */
.cover-band{left:568px;top:0;width:268px;height:254px;background:var(--yellow)}
.brand{left:620px;top:40px;width:164px;text-align:center;font-family:"Cabin Condensed",Arial,sans-serif;font-weight:700;color:var(--ink);font-size:17px;line-height:19px;display:flex;align-items:center;gap:7px;justify-content:center}
.brand .mark{width:10px;height:10px;border-radius:50%;background:var(--ink);flex:none}
.food-photo{left:607px;top:104px;width:188px;height:188px;border-radius:50%;background:radial-gradient(circle at 48% 45%,#b46a33 0,#7a3f1e 32%,#2a1e18 58%,#111 72%)}
.cover-title{left:568px;top:347px;width:268px;text-align:center;font-family:"Montserrat",Arial,sans-serif;font-weight:900;line-height:47px}
.cover-title .food{color:var(--yellow);font-size:56px;display:block}
.cover-title .menu{color:var(--cyan);font-size:56px;display:block}
.cover-rule{left:614px;top:445px;width:176px;height:2px;background:var(--white)}
.cover-order{left:568px;top:463px;width:268px;text-align:center;font-family:"Righteous",Arial,sans-serif}
.cover-order h3{color:var(--yellow);font-weight:400;font-size:22.5px;line-height:24px;letter-spacing:.5px}
.cover-order p{font-size:15px;line-height:19px}

/* inside */
.salads{left:27px;top:16px;width:210px;height:473px;padding:10px 10px 0 10px}
.salads .entry{margin-bottom:11px}
.salads .item{font-size:7.4px}
.salads .list-head{font-size:7.4px;font-weight:600}
.starters{left:300px;top:16px;width:210px;height:473px;padding:11px 10px 0 10px}
.starters h4{font-size:8px;font-weight:700;letter-spacing:.2px;margin:12px 0 3px;border-bottom:none}
.starters .item{font-size:7px;line-height:9.6px}
.starters .gap{height:6px}
.soups{left:567px;top:2px;width:209px;height:149px;padding:16px 12px 0 14px}
.soups .entry{margin-bottom:9px}
.soups .item{font-size:7px}
.burgers-title{left:582px;top:159px;line-height:21px}
.burgers-intro{left:582px;top:203px;width:223px;font-size:7px;line-height:9.8px;color:var(--muted)}
.icon-pill{left:739px;top:288px;width:78px;height:18px;background:var(--white);border-radius:9px;display:flex;justify-content:space-around;align-items:center;z-index:2}
.icon-pill svg{width:11px;height:11px}
.burger-table{left:575px;top:297px;width:251px;height:198px;padding:14px 8px 0 8px}
.burger-table table{width:100%;border-collapse:collapse}
.burger-table td{vertical-align:top;padding-bottom:7px}
.burger-table .name{font-size:5.6px;font-weight:700;line-height:7px}
.burger-table .price{font-size:5px;width:28px;text-align:left;color:#e8e8e8;padding-top:1px}
</style>
</head>
<body>

<!-- OUTSIDE -->
<section class="sheet sheet--outside" aria-label="Outside of the tri-fold">

  <div class="paw-field" style="left:13px;top:13px;width:44px;height:138px" role="img" aria-label="Trail of paw prints"></div>
  <div class="placeholder-yellow" style="left:0;top:174px;width:65px;height:64px" role="img" aria-label="Sitting cat silhouette"></div>

  <div class="box handhelds">
    <h2 class="section-title">OTHER HANDHELDS:</h2>
    <p class="intro">All served with Hand Cut Fries or Sweet Potato Fries.<br>Premium sides available for an up charge +2</p>
    <div class="entry"><div class="item"><span>Cat Club</span><span class="dots"></span><span>15</span></div>
      <p class="desc">Sliced whole wheat bread with roasted garlic aioli, grilled marinated chicken breast, provolone cheese bacon, lettuce and tomato.</p></div>
    <div class="entry"><div class="item"><span>Southwest Melt</span><span class="dots"></span><span>14</span></div>
      <p class="desc">Sliced whole wheat bread with roasted garlic aioli,3 pepper colby jack, roasted red peppers and corn.</p></div>
    <div class="entry"><div class="item"><span>What's Gouda?</span><span class="dots"></span><span>14</span></div>
      <p class="desc">Sliced whole wheat bread with roasted garlic aioli smoked gouda and provolone cheeses, roasted red peppers and portobello mushrooms.</p></div>
    <div class="entry"><div class="item"><span>Westover Melt</span><span class="dots"></span><span>14</span></div>
      <p class="desc">Sliced whole wheat bread with roasted garlic aioli, zucchini, portobello mushrooms, red peppers, with melted brie and provolone cheeses.</p></div>
  </div>

  <div class="outlined" style="left:37px;top:257px;width:87px;height:42px">
    <h4>CHEESES:</h4>
    <p>Vermont Cheddar | Smoked Gouda<br>3-Pepper Colby Jack<br>Monterey Jack | Swiss | Brie<br>Provolone | American</p>
  </div>
  <div class="outlined" style="left:127px;top:257px;width:101px;height:42px">
    <h4>TOPPINGS:</h4>
    <p>Bacon | Shrimp | Egg | Red Onion | White Onion | Portobello Mushrooms | Roasted Corn | Roasted Red Peppers Guacamole | Pico De Gallo | Fresh or Pickled Jalapenos</p>
  </div>
  <div class="outlined" style="left:37px;top:308px;width:128px;height:36px">
    <h4>CONDIMENTS:</h4>
    <p>Horseradish Aioli | Chipotle Crema | Roasted Garlic Aioli | Citrus Aioli Spicy Ketchup | Dijon Mustard | Yellow Mustard | Mayo | Ketchup</p>
  </div>
  <div class="placeholder-yellow" style="left:182px;top:280px;width:66px;height:66px" role="img" aria-label="Walking cat silhouette"></div>

  <div class="box sides">
    <h2 class="section-title">SIDES:</h2>
    <p>Potato Salad $4 &nbsp;| Fire Roasted Veggies $6<br>Brown Rice, Quinoa, &amp; Kale Medley $5</p>
  </div>

  <div class="paw-field" style="left:226px;top:358px;width:47px;height:138px" role="img" aria-label="Trail of paw prints"></div>

  <div class="box kids">
    <h2 class="section-title">KIDS MENU:</h2>
    <p class="sub">All served with French Fries</p>
    <div class="item"><span>Grilled Cheese</span><span class="dots"></span><span>8</span></div>
    <div class="item"><span>Cheese Quesadilla</span><span class="dots"></span><span>8</span></div>
    <div class="item"><span>Mac &amp; Cheese</span><span class="dots"></span><span>8</span></div>
    <div class="item"><span>Chicken Tenders</span><span class="dots"></span><span>10</span></div>
  </div>

  <p class="footnote" style="left:34px;top:509px">*The consumption of raw or undercooked eggs, meat, poultry, seafood or shellfish may contribute to food borne illness, especially if you have a medical condition.<br>- Vegetarian &nbsp;- Spicy</p>

  <div class="abs happy">
    <h2><span class="l1">HAPPY HOUR</span><br><span class="l2">SPECIALS</span></h2>
  </div>

  <div class="box lorem-box">
    <p>Lorem ipsum dolor sit amet, consectetuer adipiscing elit, sed diam nonummy nibh euismod tincidunt ut laoreet dolore magna aliquam erat volutpat. Ut wisi enim ad</p>
    <p>Lorem ipsum dolor sit amet, consectetuer adipiscing elit, sed diam nonummy nibh euismod tincidunt ut laoreet dolore magna aliquam erat volutpat. Ut wisi enim ad</p>
    <p>Lorem ipsum dolor sit amet, consectetuer adipiscing elit, sed diam nonummy nibh euismod tincidunt ut laoreet dolore magna aliquam erat volutpat. Ut wisi enim ad</p>
  </div>

  <div class="promo promo--yellow">Lorem ipsum dolor sit amet, consectetuer adipiscing elit, sed diam nonummy nibh euismod tincidunt ut laoreet dolore magna aliquam erat volutpat. Ut wisi enim ad Lorem ipsum dolor sit amet, consectetuer adipiscing elit, sed diam nonummy nibh euismod tincidunt ut laoreet dolore.</div>
  <div class="promo promo--cyan">Lorem ipsum dolor sit amet, consectetuer adipiscing elit, sed diam nonummy nibh euismod tincidunt ut laoreet dolore magna aliquam erat volutpat. Ut wisi enim ad Lorem ipsum dolor sit amet, consectetuer adipiscing elit, sed diam nonummy nibh euismod tincidunt ut laoreet dolore.</div>

  <p class="abs lorem-para">Lorem ipsum dolor sit amet, consectetuer adipiscing elit, sed diam nonummy nibh euismod tincidunt ut laoreet dolore magna aliquam erat volutpat. Ut wisi enim ad Lorem ipsum dolor sit amet, consectetuer adipiscing elit, sed diam nonummy nibh euismod tincidunt ut laoreet dolore magna aliquam erat volutpat. Ut wisi enim ad</p>

  <div class="abs delivery-band">
    <svg class="abs" style="left:0;top:0" width="267" height="117" viewBox="0 0 267 117" aria-hidden="true">
      <polygon points="0,0 133,24 267,0 267,117 0,117" fill="var(--yellow)"/>
    </svg>
    <div class="placeholder-dark" style="left:12px;top:36px;width:58px;height:64px" role="img" aria-label="Sitting cat silhouette"></div>
    <div class="text">
      <h3>ORDER DELIVERY</h3>
      <p class="url">WWW.COPPERHERONGRILL.COM</p>
      <p class="phone">555-014-7720</p>
    </div>
  </div>

  <div class="abs cover-band"></div>
  <div class="abs brand"><span class="mark"></span><span>Copper Heron<br>Bar &amp; Grill</span></div>
  <div class="placeholder-dark" style="left:588px;top:97px;width:20px;height:20px" role="img" aria-label="Paw print"></div>
  <div class="placeholder-dark" style="left:766px;top:97px;width:20px;height:20px" role="img" aria-label="Paw print"></div>
  <div class="abs food-photo" role="img" aria-label="Photo of a grilled steak with roasted potatoes, tomatoes and lemon in a black pan"></div>
  <svg class="abs" style="left:596px;top:266px" width="204" height="48" viewBox="0 0 204 48" aria-hidden="true">
    <path d="M2 2 Q102 86 202 2" fill="none" stroke="var(--white)" stroke-width="1.3"/>
  </svg>
  <h1 class="abs cover-title"><span class="food">FOOD</span><span class="menu">MENU</span></h1>
  <div class="abs cover-rule"></div>
  <div class="abs cover-order">
    <h3>ORDER DELIVERY</h3>
    <p>WWW.COPPERHERONGRILL.COM</p>
    <p>555-014-7720</p>
  </div>
</section>

<!-- INSIDE -->
<section class="sheet sheet--inside" aria-label="Inside of the tri-fold">

  <div class="box salads">
    <h2 class="section-title" style="margin-bottom:20px">SALADS</h2>
    <div class="entry"><div class="item"><span>Combo Cat</span><span class="dots"></span><span>11</span></div>
      <p class="desc">Enjoy a side House and a cup of any soup.</p></div>
    <div class="entry" style="margin-top:14px"><div class="item"><span>Cat House Salad</span><span class="dots"></span><span>11</span></div>
      <p class="desc">Spring lettuce mix, fresh red peppers, onion, cherry tomatoes, cucumber, and croutons. Served with Red Wine Vinaigrette.</p></div>
    <div class="entry"><div class="item"><span>Grilled Chicken Salad</span><span class="dots"></span><span>15</span></div>
      <p class="desc">Spring lettuce mix, grilled chicken breast, bacon,<br>fresh red peppers, onions, tomatoes, cucumber and<br>feta cheese. Served with Red Wine Vinaigrette</p></div>
    <div class="entry"><div class="item"><span>Grilled Shrimp Salad*</span><span class="dots"></span><span>16</span></div>
      <p class="desc">Spring lettuce mix, garlic Roasted Shrimp, roasted corn,<br>pico de gallo fresh avocado, Served with<br>Lemon Champagne Vinaigrette</p></div>
    <div class="entry"><div class="item"><span>Goat Cheese Salad</span><span class="dots"></span><span>16</span></div>
      <p class="desc">Spring lettuce mix, fried goat cheese, fresh red peppers,<br>cranberries, white onions, and cherry tomatoes.<br>Served with Lemon Champagne Vinaigrette.</p></div>
    <div class="entry"><div class="item"><span>The Skinny Cat</span><span class="dots"></span><span>14</span></div>
      <p class="desc">Spring lettuce mix, sliced apple, sun dried cranberries,<br>roasted corn, cherry tomatoes, and feta cheese.<br>Served with Balsamic Vinaigrette.</p></div>
    <div class="entry" style="width:170px"><div class="item"><span>Small House Salad</span><span class="dots"></span><span>6</span></div></div>
    <p class="list-head" style="margin-top:26px;line-height:10px">Add: &nbsp;Grilled Chicken &nbsp;5 | Garlic Roasted Shrimp 5<br>Fried Goat Cheese 4 , Fried Goat Cheese 5</p>
    <p class="list-head" style="margin-top:10px">Dressings</p>
    <p class="desc" style="line-height:10px">Balsamic Vinaigrette | Caesar | Red Wine Vinaigrette<br>Honey-Mustard | Lemon Champagne Vinaigrette<br>Ranch | Blue Cheese</p>
  </div>
  <div class="placeholder-yellow" style="left:220px;top:416px;width:59px;height:60px" role="img" aria-label="Kitten silhouette"></div>
  <div class="paw-field" style="left:242px;top:268px;width:44px;height:144px" role="img" aria-label="Trail of paw prints"></div>

  <div class="box starters">
    <h2 class="section-title">STARTERS</h2>
    <h4>TORTILLA CHIPS:</h4>
    <div class="item"><span>with House-made Salsa Verde</span><span class="dots"></span><span>7</span></div>
    <div class="item"><span>with House-made Fire Roasted Salsa</span><span class="dots"></span><span>7</span></div>
    <div class="item"><span>with Guacamole &amp; Pico De Gallo</span><span class="dots"></span><span>8</span></div>
    <div class="item"><span>with Queso</span><span class="dots"></span><span>8</span></div>
    <div class="item"><span>with Chili con Queso</span><span class="dots"></span><span>9</span></div>
    <h4>WINGS:</h4>
    <div class="item"><span>8 pieces</span><span class="dots"></span><span>14</span></div>
    <p class="small-desc">Flash-fried to a crispy golden brown and tossed in your choice of sauce. Choose from our Signature Hot, or Mild Sauce, or BBQ. Your choice of ranch or blue cheese.</p>
    <h4>QUESADILLAS:</h4>
    <div class="item"><span>Cheddar and Monterey Jack Cheese</span><span class="dots"></span><span>12</span></div>
    <div class="item"><span>Pulled Marinated Chicken &amp; Cheese</span><span class="dots"></span><span>16</span></div>
    <div class="item"><span>Fire Roasted Vegetables &amp; Cheese</span><span class="dots"></span><span>14</span></div>
    <div class="item"><span>Garlic Roasted Shrimp &amp; Cheese</span><span class="dots"></span><span>16</span></div>
    <p class="small-desc">All quesadillas are stuffed with roasted red peppers, black beans, and your choice of cheese. Served with guacamole, pico de gallo, and chipotle crema on the side.</p>
    <h4>CLAW-FULL NACHOS:</h4>
    <p class="small-desc">Tortilla chips, melted white queso, Cheddar and Monterey Jack cheeses, pico de gallo, guacamole, chipotle sour cream, jalapenos, black beans, &amp; green onions</p>
    <div class="item" style="margin-top:3px"><span>Copper Heron Chili Nachos</span><span class="dots"></span><span>14</span></div>
    <div class="gap"></div>
    <div class="item"><span>Pulled Chicken Nachos</span><span class="dots"></span><span>16</span></div>
    <div class="gap"></div>
    <div class="item"><span>Garlic Roasted Shrimp</span><span class="dots"></span><span>16</span></div>
    <div class="gap"></div>
    <div class="item"><span>Fire Roasted Vegetables Nachos</span><span class="dots"></span><span>14</span></div>
    <p class="desc">Portobello, Red Peppers, &amp; Zucchini</p>
    <h4 style="margin-top:6px">FRENCH FRIES:</h4>
    <p class="desc">Served with our house made Garlic Aioli and Spicy Ketchup.</p>
    <div class="item" style="margin-top:3px"><span>Fries Only</span><span class="dots"></span><span>7</span></div>
    <div class="gap" style="height:4px"></div>
    <div class="item"><span>Sweet Potato Fries</span><span class="dots"></span><span>7</span></div>
    <div class="gap" style="height:4px"></div>
    <div class="item"><span>Cheddar-Jack Cheese Fries</span><span class="dots"></span><span>8</span></div>
    <div class="gap" style="height:4px"></div>
    <div class="item"><span>Cheddar-Jack Cheese, Bacon Fries</span><span class="dots"></span><span>9</span></div>
    <div class="gap" style="height:4px"></div>
    <div class="item"><span>Chili Cheese Fries</span><span class="dots"></span><span>10</span></div>
    <p class="small-desc">Topped with Copper Heron Chili, cheddar jack cheese and served with chipotle crema on the side.</p>
  </div>
  <div class="placeholder-yellow" style="left:443px;top:21px;width:106px;height:44px" role="img" aria-label="Prowling cat silhouette"></div>
  <div class="paw-field" style="left:516px;top:68px;width:47px;height:138px" role="img" aria-label="Trail of paw prints"></div>

  <div class="box soups">
    <div class="entry"><div class="item"><span>Copper Heron Chili</span><span class="dots"></span><span>Cup 6 | Bowl 8</span></div>
      <p class="small-desc">Copper Heron Signature Chili with lean ground beef, black beans, and corn. Topped with cheddar cheese and green onion, served with tri-color tortilla chips.</p></div>
    <div class="entry"><div class="item"><span>Southwestern Sweet Potato Soup &nbsp;......&nbsp; Cup 6 | Bowl 8</span></div>
      <p class="small-desc">A delicious mix of sweet potatoes, corn, bell peppers, and black beans, this vegan soup delivers top flavor and quality with every bowl. Served with tri-color tortilla chips.</p></div>
    <div class="entry"><div class="item"><span>Ancient Grains Bowl</span><span class="dots"></span><span>12</span></div>
      <p class="small-desc">Quinoa, brown rice, kale and fresh spinach, with fire roasted portobello mushrooms, zucchini and red peppers. Topped with fresh avocado, and feta cheese. Served with Lemon Champagne Vinaigrette</p></div>
    <p class="item">Add: &nbsp;Grilled Chicken &nbsp;5 | Garlic Roasted Shrimp 5</p>
  </div>

  <h2 class="abs section-title burgers-title">GOURMET BURGERS &amp;<br>SANDWICHES</h2>
  <p class="abs burgers-intro">Start with your style and then choose your protein. Our burgers are house made and cooked to your temperature. Our Fresh grilled chicken breast is marinated in house and cooked to perfection. Keep it vegetarian by choosing a vegetarian style along with the Quinoa Lentil Burger. All are served on a potato bun with lettuce, tomato, onion, and your choice of hand cut fries or sweet potato fries. Premium sides available for an up charge + $2</p>

  <div class="abs icon-pill" aria-label="Protein columns: beef, chicken, vegetarian">
    <svg viewBox="0 0 12 12" aria-hidden="true"><circle cx="6" cy="6" r="4.5" fill="var(--ink)"/></svg>
    <svg viewBox="0 0 12 12" aria-hidden="true"><circle cx="6" cy="6" r="4.5" fill="var(--ink)"/></svg>
    <svg viewBox="0 0 12 12" aria-hidden="true"><circle cx="6" cy="6" r="4.5" fill="none" stroke="var(--ink)" stroke-width="1.2"/><path d="M4 4.5 6 8 8 4.5" fill="none" stroke="var(--ink)" stroke-width="1.1"/></svg>
  </div>
  <div class="box burger-table">
    <table>
      <tr><td><p class="name">Calico Cat</p><p class="small-desc">Roasted red peppers, red onions, brie cheese, and horseradish aioli.</p></td><td class="price">15.00*</td><td class="price">14.00</td><td class="price">13.00</td></tr>
      <tr><td><p class="name">Tiger Cat</p><p class="small-desc">Cheddar, Monterey Jack, and Provolone</p></td><td class="price">15.00*</td><td class="price">14.00</td><td class="price">13.00</td></tr>
      <tr><td><p class="name">Cat Scratch Fever</p><p class="small-desc">Guacamole, 3 pepper colby jack, pico de gallo, and chipotle mayo.</p></td><td class="price">15.50*</td><td class="price">15.00</td><td class="price">14.00</td></tr>
      <tr><td><p class="name">The Fat Cat</p><p class="small-desc">Fried egg*, bacon, cheddar cheese, and garlic aioli.</p></td><td class="price">16.00*</td><td class="price">15.50</td><td class="price">14.50</td></tr>
      <tr><td><p class="name">Tabby Cat</p><p class="small-desc">Melted brie cheese, sliced apple, and citrus aioli.</p></td><td class="price">16.50*</td><td class="price">15.50</td><td class="price">14.50</td></tr>
      <tr><td><p class="name">The Sphynx</p><p class="small-desc">Portobello mushrooms, roasted red peppers, smoked gouda cheese, and roasted garlic aioli.</p></td><td class="price">16.50*</td><td class="price">15.50</td><td class="price">14.50</td></tr>
      <tr><td><p class="name">Maine Coon</p><p class="small-desc">Grilled shrimp*, roasted corn, swiss cheese, and roasted garlic aioli.</p></td><td class="price">16.50*</td><td class="price">15.50</td><td class="price">14.50</td></tr>
      <tr><td><p class="name">Alley Cat</p><p class="small-desc">What up your alley? Choose a cheese, condiment and one topping. Additional Toppings $1 | Bacon, Egg, Shrimp - $2</p></td><td class="price">14.00*</td><td class="price">13.00</td><td class="price">12.00</td></tr>
    </table>
  </div>

  <p class="footnote" style="left:38px;top:511px">*The consumption of raw or undercooked eggs, meat, poultry, seafood or shellfish may contribute to food borne illness, especially if you have a medical condition.<br>- Vegetarian &nbsp;- Spicy</p>
  <p class="footnote" style="left:318px;top:511px">*The consumption of raw or undercooked eggs, meat, poultry, seafood or shellfish may contribute to food borne illness, especially if you have a medical condition.<br>- Vegetarian &nbsp;- Spicy</p>
  <p class="footnote" style="left:598px;top:511px">*The consumption of raw or undercooked eggs, meat, poultry, seafood or shellfish may contribute to food borne illness, especially if you have a medical condition.<br>- Vegetarian &nbsp;- Spicy</p>
</section>

</body>
</html>
```